Delvin & Associates - London New Letting and Property Management Company *

Delvin & Associates LTD is a new company based in London, and works with brand new residential property in the city centre.

We are aiming to have 1000 new properties a year.

We are looking for something modern and minimalistic :
Logo ,Monogram, Paper Head and Business Card.

Target Market(s)

Internation landlords

Industry/Entity Type

Real Estate

Logo Text

Delvin & Associates

Colors

Designer to choose colors to be used in the design.

Requirements
Nice to have
• A particular monogram with "DA"
Should not have
• Little House over the logo

```html
<!DOCTYPE html>
<html lang="en">
<head>
<meta charset="utf-8">
<title>Delvin &amp; Associates – Business Card</title>
<link rel="stylesheet" href="https://fonts.googleapis.com/css2?family=Montserrat:wght@400;600;700&display=swap">
<style>
  :root {
    --backdrop: #3b3431;
    --card: #141517;
    --ink: #ffffff;
    --accent: #2a93d5;
    --muted: #d9dde0;
  }
  * { box-sizing: border-box; margin: 0; padding: 0; }
  html, body { width: 1200px; height: 715px; overflow: hidden; }
  body {
    background: var(--backdrop);
    font-family: "Montserrat", Arial, sans-serif;
    color: var(--ink);
    position: relative;
  }
  .card {
    position: absolute;
    top: 209px;
    width: 520px;
    height: 297px;
    background: var(--card);
    border-radius: 6px;
    box-shadow: 0 10px 30px rgba(0,0,0,.45);
  }
  .card--front { left: 55px; border-bottom: 5px solid var(--accent); }
  .card--back { left: 625px; }

  .brand {
    position: absolute;
    display: flex;
    flex-direction: column;
    align-items: center;
    white-space: nowrap;
  }
  .brand__row { display: flex; align-items: center; gap: 10px; }
  .brand__square { width: 14px; height: 14px; background: var(--ink); flex: none; }
  .brand__name, .brand__suffix { font-weight: 600; color: var(--ink); }
  .brand__sub { display: flex; align-items: center; gap: 10px; margin-top: 4px; }
  .brand__rule { height: 2px; background: var(--accent); }

  .card--front .brand { left: 50%; top: 50%; transform: translate(-50%, -50%); }
  .card--front .brand__name { font-size: 28px; }
  .card--front .brand__suffix { font-size: 16px; letter-spacing: 2px; }
  .card--front .brand__rule { width: 90px; }

  .card--back .brand { left: 0; width: 255px; top: 148px; transform: translateY(-50%); }
  .card--back .brand__square { width: 11px; height: 11px; }
  .card--back .brand__row { gap: 8px; }
  .card--back .brand__name { font-size: 16px; }
  .card--back .brand__suffix { font-size: 11px; letter-spacing: 1.5px; }
  .card--back .brand__rule { width: 55px; }

  .divider {
    position: absolute;
    left: 255px; top: 48px;
    width: 2px; height: 200px;
    background: var(--accent);
  }
  .contact { position: absolute; left: 280px; top: 52px; }
  .contact__name { font-size: 17px; font-weight: 700; color: var(--accent); letter-spacing: .3px; }
  .contact__role { font-size: 13px; color: var(--accent); margin-bottom: 12px; }
  .contact__list { list-style: none; }
  .contact__item {
    display: flex; align-items: center; gap: 8px;
    font-size: 13px; line-height: 20px; color: var(--muted);
  }
  .contact__item svg { width: 11px; height: 11px; flex: none; }
  .contact__item .link { color: var(--accent); }
  .contact__address { font-size: 13px; line-height: 20px; color: var(--muted); margin-top: 4px; }
</style>
</head>
<body>
  <section class="card card--front">
    <div class="brand">
      <div class="brand__row">
        <span class="brand__square"></span>
        <span class="brand__name">Delvin &amp; Associates</span>
      </div>
      <div class="brand__sub">
        <span class="brand__rule"></span>
        <span class="brand__suffix">LTD</span>
        <span class="brand__rule"></span>
      </div>
    </div>
  </section>

  <section class="card card--back">
    <div class="brand">
      <div class="brand__row">
        <span class="brand__square"></span>
        <span class="brand__name">Delvin &amp; Associates</span>
      </div>
      <div class="brand__sub">
        <span class="brand__rule"></span>
        <span class="brand__suffix">LTD</span>
        <span class="brand__rule"></span>
      </div>
    </div>
    <div class="divider"></div>
    <div class="contact">
      <p class="contact__name">OWEN HARTLEY</p>
      <p class="contact__role">Founder</p>
      <ul class="contact__list">
        <li class="contact__item">
          <svg viewBox="0 0 12 12"><rect x="3" y="0.5" width="6" height="11" rx="1" fill="none" stroke="var(--accent)" stroke-width="1.2"/><circle cx="6" cy="9.5" r=".7" fill="var(--accent)"/></svg>
          020. 555. 0142
        </li>
        <li class="contact__item">
          <svg viewBox="0 0 12 12"><path d="M2.5 1 L4.5 1 L5 3.5 L3.8 4.5 Q5 7 7.5 8.2 L8.5 7 L11 7.5 L11 9.5 Q11 11 9.5 11 Q1 10 1 2.5 Q1 1 2.5 1 Z" fill="var(--accent)"/></svg>
          020. 555. 0198
        </li>
        <li class="contact__item">
          <svg viewBox="0 0 12 12"><rect x="0.6" y="2" width="10.8" height="8" fill="none" stroke="var(--accent)" stroke-width="1.2"/><path d="M1 2.5 L6 6.5 L11 2.5" fill="none" stroke="var(--accent)" stroke-width="1.2"/></svg>
          info@delvinassociates.co.uk
        </li>
        <li class="contact__item">
          <svg viewBox="0 0 12 12"><circle cx="6" cy="6" r="5.2" fill="none" stroke="var(--accent)" stroke-width="1.2"/><ellipse cx="6" cy="6" rx="2.2" ry="5.2" fill="none" stroke="var(--accent)" stroke-width="1"/><path d="M1 6 H11" stroke="var(--accent)" stroke-width="1"/></svg>
          <span>www.<span class="link">delvinassociates</span>.co.uk</span>
        </li>
      </ul>
      <p class="contact__address">48 Carrow Lane<br>London, EC2A 4NB</p>
    </div>
  </section>
</body>
</html>
```